Kestrel Arc Services business card Design

I need a business card that will wow clients at first sight.

Kestrel Arc Services connects people with HOME & LIFESTYLE SERVICES, and the client pays the value that was created by our service, using. 'Pay What You Think It's Worth".
Please look us up at www.kestrelarcservices.com to see our mission and services.

The new website is being launched in 8 weeks.

I need a business card to campaign LANDSCAPING however please design it to be easily modified to CLEANING SERVICE, PLUMBING Etc Etc.

Until our SEO campaign begins working I need business cards to leave with prospective clients for each individual service as appropriate.

Orla Pemberton
Creative Director
www.kestrelarcservices.com
1-888-617-4KAS
email: info@kestrelarcservices.com

Target Market(s)

Residential and commercial clients

Industry/Entity Type

Business

Contact Information for Business Card

2 sided

Font styles to use
Sans Serif

Requirements
Must have
• Im prefering a black card so far
• Logo
• "Pay what You Think It's Worth" seal
• Complete Landscaping & Construction
• Trundler Services
• Contact details
• facebook kestrelarc services
• twitter @kestrelarc services
• Adaptable card easily to different services we offer at Kestrel Arc Services as per www.kestrelarcservices.com
Should not have
• Too much imagery

```html
<!DOCTYPE html>
<html lang="en">
<head>
<meta charset="utf-8">
<title>Kestrel Arc Services – Business Card</title>
<link href="https://fonts.googleapis.com/css2?family=Open+Sans:wght@400;600;700&display=swap" rel="stylesheet">
<style>
  :root {
    --backdrop: #5e3b27;
    --card: #232323;
    --text-grey: #c4c4c4;
    --brand-grey: #b3b3b3;
    --name-blue: #3b6bc8;
    --green: #7ac143;
    --teal: #1f8ea8;
    --blue: #3b63c4;
    --purple: #7a4fc0;
    --seal-fill: #3d3d3d;
  }
  * { box-sizing: border-box; margin: 0; padding: 0; }
  html, body { width: 1200px; height: 1000px; overflow: hidden; }
  body {
    background: var(--backdrop);
    font-family: "Open Sans", Arial, sans-serif;
    position: relative;
  }
  .card {
    position: absolute;
    left: 265px;
    width: 665px;
    height: 397px;
    background: var(--card);
    overflow: hidden;
    box-shadow: 0 6px 18px rgba(0,0,0,0.45);
  }
  .card--front { top: 73px; }
  .card--back { top: 533px; }

  .brand {
    position: absolute;
    display: flex;
    align-items: center;
    gap: 12px;
  }
  .brand__dot {
    width: 40px; height: 40px; border-radius: 50%;
    background: var(--blue);
  }
  .brand__name {
    font-size: 28px;
    font-weight: 400;
    color: var(--brand-grey);
    white-space: nowrap;
  }
  .card--front .brand { left: 35px; top: 62px; }
  .card--back .brand { left: 35px; top: 300px; }

  .contact { position: absolute; left: 133px; top: 163px; }
  .contact__name { font-size: 20px; font-weight: 700; color: var(--name-blue); line-height: 1.2; }
  .contact__role { font-size: 16px; color: var(--text-grey); margin-bottom: 12px; }
  .contact__line {
    font-size: 16px; color: var(--text-grey);
    display: flex; align-items: center; gap: 7px;
    height: 24.5px;
    white-space: nowrap;
  }
  .contact__line svg { width: 16px; height: 16px; fill: var(--name-blue); flex: none; }
  .contact__social { margin-top: 7px; }
  .contact__my { color: var(--name-blue); }
  .social-dot { width: 16px; height: 16px; border-radius: 50%; background: var(--name-blue); flex: none; }

  .seal {
    position: absolute; left: 30px; top: 266px;
    width: 84px; height: 84px; border-radius: 50%;
    background: var(--seal-fill);
  }

  .services { position: absolute; right: 0; top: 0; width: 260px; height: 100%; }
  .service {
    position: absolute; right: 34px;
    font-size: 16px; text-align: right; line-height: 1.25;
    transform: translateY(-50%);
    white-space: nowrap;
  }
  .service__dot {
    position: absolute; right: -16px;
    width: 32px; height: 32px; border-radius: 50%;
    transform: translateY(-50%);
  }
  .is-green { color: var(--green); } .bg-green { background: var(--green); }
  .is-teal { color: var(--teal); } .bg-teal { background: var(--teal); }
  .is-blue { color: var(--blue); } .bg-blue { background: var(--blue); }
  .is-purple { color: var(--purple); } .bg-purple { background: var(--purple); }
</style>
</head>
<body>

<section class="card card--front" aria-label="Business card front">
  <div class="brand">
    <span class="brand__dot"></span>
    <span class="brand__name">Kestrel Arc Services Inc.</span>
  </div>

  <div class="contact">
    <p class="contact__name">Orla Pemberton</p>
    <p class="contact__role">Creative Director</p>
    <p class="contact__line">
      <svg viewBox="0 0 16 16"><path d="M3 2h3l1 3-2 1a8 8 0 0 0 5 5l1-2 3 1v3a1 1 0 0 1-1 1A12 12 0 0 1 2 3a1 1 0 0 1 1-1z"/></svg>
      1-888-617-4KAS
    </p>
    <p class="contact__line">
      <svg viewBox="0 0 16 16"><path d="M1 3h14v10H1z M2 4l6 5 6-5" fill="none" stroke="#3b6bc8" stroke-width="1.6"/></svg>
      info@kestrelarcservices.com
    </p>
    <p class="contact__line">
      <svg viewBox="0 0 16 16"><circle cx="8" cy="8" r="6.5" fill="none" stroke="#3b6bc8" stroke-width="1.6"/><path d="M1.5 8h13M8 1.5c-3 3.5-3 9.5 0 13M8 1.5c3 3.5 3 9.5 0 13" fill="none" stroke="#3b6bc8" stroke-width="1.2"/></svg>
      www.kestrelarcservices.com
    </p>
    <div class="contact__social">
      <p class="contact__line"><span class="contact__my">My</span><span class="social-dot"></span>kestrelarc services</p>
      <p class="contact__line"><span class="contact__my">My</span><span class="social-dot"></span>@kestrelarc services</p>
    </div>
  </div>

  <div class="seal" role="img" aria-label="Pricing promise badge"></div>

  <div class="services">
    <p class="service is-green" style="top:64px">Landscaping<br>Construction</p>
    <span class="service__dot bg-green" style="top:64px"></span>
    <p class="service is-teal" style="top:139px">Trundler</p>
    <span class="service__dot bg-teal" style="top:139px"></span>
    <p class="service is-blue" style="top:207px">Cleaning</p>
    <span class="service__dot bg-blue" style="top:207px"></span>
    <p class="service is-purple" style="top:277px">Plumbing</p>
    <span class="service__dot bg-purple" style="top:277px"></span>
    <p class="service is-teal" style="top:343px">Remodeling</p>
    <span class="service__dot bg-teal" style="top:343px"></span>
  </div>
</section>

<section class="card card--back" aria-label="Business card back">
  <div class="brand">
    <span class="brand__dot"></span>
    <span class="brand__name">Kestrel Arc Services Inc.</span>
  </div>
</section>

</body>
</html>
```